Corvale Holdings Business Cards

Hello. I need business cards designed with our new logo. I'd like to see at least 3 different designs. At least one with a dark background, and at least one with a white background. Maybe one with gray or blue for the background. Play with gradient colors and maybe even insert a pic of a skyline in the background of one or more of them. Use your judgement. We will need 2 cards printed. They need to accommodate the employee name, title, company address, phone, email, and website. Thanks.

Target Market(s)

Wealthy mature investors.

Contact Information for Business Card

Single-sided, professional, clean design that incorporates our logo.

Font styles to use
Sans Serif

Requirements
Must have
• Our new logo needs to be featured on it. (See attached.)
• Employee Name (In all CAPS)
• Title
• Street Address, City, ST Zip Code
• Cell Phone #, Email Address, Website Address
Nice to have
• Design that blends well with our new logo and its colors, or a city scape or other graphic design that looks like an apartment complex in the background. Blues and grays are nice, but use your judgement.
Should not have
• Modern or oriental looking designs or bright colors.

```html
<!DOCTYPE html>
<html lang="en">
<head>
<meta charset="utf-8">
<title>Corvale Holdings Business Cards</title>
<link rel="stylesheet" href="https://fonts.googleapis.com/css2?family=Questrial&family=Lato:wght@400&display=swap">
<style>
  :root {
    --backdrop: #2e2e30;
    --card-white: #ffffff;
    --brand-blue: #25a6de;
    --brand-gray: #6a6b6d;
    --text-gray: #555659;
    --rule-gray: #c9c9c9;
  }
  * { margin: 0; padding: 0; box-sizing: border-box; }
  html, body {
    width: 1200px; height: 1200px; overflow: hidden;
    background: var(--backdrop);
  }
  .canvas { position: relative; width: 1200px; height: 1200px; }
  .card {
    position: absolute; top: 310px; height: 594px;
  }
  .card--front { left: 234px; width: 364px; background: var(--card-white); }
  .card--back { left: 627px; width: 369px; background: var(--brand-gray); }

  .wordmark {
    position: absolute; top: 157px; left: 0; width: 100%;
    display: flex; align-items: center; justify-content: center; gap: 12px;
  }
  .wordmark__square { width: 18px; height: 18px; background: var(--brand-blue); }
  .wordmark__name {
    font-family: "Questrial", sans-serif; font-size: 26px; line-height: 1.1;
    color: var(--brand-blue); letter-spacing: 1px; text-transform: uppercase;
  }

  .person {
    position: absolute; top: 332px; width: 100%; text-align: center;
  }
  .person__name {
    font-family: "Questrial", sans-serif; font-size: 26px; color: var(--brand-blue);
    letter-spacing: 0.3px; line-height: 30px;
  }
  .person__title {
    font-family: "Lato", sans-serif; font-size: 16px; color: var(--text-gray); line-height: 20px;
  }

  .contact-icons {
    position: absolute; top: 395px; left: 87px; width: 190px; height: 24px;
    display: flex; align-items: center; justify-content: center; gap: 4px;
  }
  .contact-icons__rule { flex: 1; height: 1px; background: var(--brand-gray); }
  .contact-icons svg { width: 24px; height: 24px; display: block; }

  .contact {
    position: absolute; top: 431px; width: 100%; text-align: center;
    font-family: "Lato", sans-serif; font-size: 16px; line-height: 22px; color: var(--text-gray);
  }
  .contact__divider {
    width: 196px; height: 1px; background: var(--rule-gray); margin: 10px auto 9px;
  }

  .back-name {
    position: absolute; top: 0; left: 0; width: 100%; height: 100%;
    display: flex; align-items: center; justify-content: center; gap: 14px;
  }
  .back-name__square { width: 22px; height: 22px; background: var(--card-white); }
  .back-name__text {
    font-family: "Questrial", sans-serif; font-size: 30px; line-height: 1.15;
    color: var(--card-white); letter-spacing: 1px; text-transform: uppercase;
  }
</style>
</head>
<body>
<main class="canvas">
  <section class="card card--front">
    <div class="wordmark">
      <span class="wordmark__square"></span>
      <span class="wordmark__name">Corvale<br>Holdings, LLC</span>
    </div>

    <div class="person">
      <p class="person__name">DANIEL WHITMORE</p>
      <p class="person__title">Managing Director</p>
    </div>

    <div class="contact-icons">
      <span class="contact-icons__rule"></span>
      <svg viewBox="0 0 24 24" aria-label="Phone">
        <circle cx="12" cy="12" r="12" fill="var(--brand-blue)"/>
        <path d="M6.5 10.5c0-2 2-3 5.5-3s5.5 1 5.5 3l-2 .6-.6-1.6c-1.8-.6-4-.6-5.8 0l-.6 1.6zM8.5 12h7l1 4h-9z" fill="#fff"/>
      </svg>
      <svg viewBox="0 0 24 24" aria-label="Email">
        <circle cx="12" cy="12" r="12" fill="var(--brand-blue)"/>
        <rect x="6.5" y="8" width="11" height="8" fill="#fff"/>
        <path d="M6.5 8l5.5 4.5L17.5 8" fill="none" stroke="var(--brand-blue)" stroke-width="1.2"/>
      </svg>
      <svg viewBox="0 0 24 24" aria-label="Website">
        <circle cx="12" cy="12" r="12" fill="var(--brand-blue)"/>
        <circle cx="12" cy="12" r="5.5" fill="none" stroke="#fff" stroke-width="1.4"/>
        <path d="M6.5 12h11M12 6.5c-2.5 3-2.5 8 0 11M12 6.5c2.5 3 2.5 8 0 11" fill="none" stroke="#fff" stroke-width="1.1"/>
      </svg>
      <span class="contact-icons__rule"></span>
    </div>

    <div class="contact">
      <p>044-555 018 234</p>
      <p>info@corvaleholdings.com</p>
      <p>www.corvaleholdings.com</p>
      <div class="contact__divider"></div>
      <p>118 Harbor Lane, Suite 4,</p>
      <p>Easton, MD 21601</p>
    </div>
  </section>

  <section class="card card--back">
    <div class="back-name">
      <span class="back-name__square"></span>
      <span class="back-name__text">Corvale<br>Holdings</span>
    </div>
  </section>
</main>
</body>
</html>
```